Lift Her Forward, 2019 Save The Date

Please develop a save the date flyer our 4th Annual Lift Her Forward and See Her Rise! This event is focused on maintaining participation and appreciation for women in the design and construction industry.

This unique Forum provides a venue to engage everyone from executives to those just beginning their careers with active, hands-on sessions and vibrant networking with the best and brightest in the A/E/C industry. In our usual Q-TarVM Forum style, Keynotes become table participants and table participants become presenters, encouraging participants to assimilate what they are learning. Join local, state and national leaders and subject matter experts as we candidly explore and address the issues affecting women in our industry.

Industry/Entity Type

Construction

Font styles to use
Sans Serif

Requirements
Must have
• This is a save the date, Must have:
• Q-TarVM Logo
• Title: 4th Annual Lift Her Forward and See Her Rise!
• Date: January 25, 2019
• Location: Harbor Crest Resort and Spa, San Marcos, TX
Nice to have
• A header that can easily be pulled to add to other marketing materials and for use across other platforms (web, etc.).

```html
<!DOCTYPE html>
<html lang="en">
<head>
<meta charset="utf-8">
<title>Lift Her Forward – Save the Date</title>
<link rel="stylesheet" href="https://fonts.googleapis.com/css2?family=Lato:wght@700;900&family=Yesteryear&display=swap">
<style>
  :root {
    --stage: #b5b5b5;
    --white: #ffffff;
    --navy: #1f3f95;
    --navy-dark: #17327a;
    --green: #9cc64a;
    --green-light: #b5d96e;
    --green-dark: #7fae34;
    --slate: #58595b;
    --slate-light: #8a8b8d;
  }
  html, body {
    margin: 0;
    padding: 0;
    width: 1200px;
    height: 610px;
    overflow: hidden;
    background: var(--stage);
  }
  .flyer {
    position: absolute;
    left: 384px;
    top: 0;
    width: 432px;
    height: 610px;
    overflow: hidden;
    font-family: "Lato", Arial, sans-serif;
    background: var(--white);
  }
  .flyer-art {
    position: absolute;
    inset: 0;
  }
  .brand {
    position: absolute;
    top: 18px;
    left: 0;
    width: 100%;
    display: flex;
    justify-content: center;
    align-items: center;
    gap: 10px;
  }
  .brand-mark {
    width: 38px;
    height: 38px;
    border-radius: 50%;
    background: var(--navy);
  }
  .brand-name {
    font-weight: 700;
    font-size: 30px;
    color: var(--navy);
    letter-spacing: 0.5px;
  }
  .title {
    position: absolute;
    top: 124px;
    left: 0;
    width: 100%;
    text-align: center;
    color: var(--navy);
    margin: 0;
  }
  .title-edition {
    display: block;
    font-weight: 900;
    font-size: 56px;
    line-height: 56px;
  }
  .title-name {
    display: block;
    font-weight: 700;
    font-size: 32px;
    line-height: 36px;
  }
  .title-tagline {
    display: block;
    font-weight: 700;
    font-size: 17px;
    line-height: 22px;
  }
  .save-date {
    position: absolute;
    top: 328px;
    left: 0;
    width: 100%;
    text-align: center;
    font-family: "Yesteryear", cursive;
    color: var(--white);
    font-size: 74px;
    line-height: 62px;
    margin: 0;
  }
  .date-card {
    position: absolute;
    left: 120px;
    top: 488px;
    width: 192px;
    height: 56px;
    background: var(--white);
    transform: rotate(-3deg);
    box-shadow: 0 2px 4px rgba(0,0,0,0.25);
    display: flex;
    align-items: center;
    justify-content: center;
    gap: 6px;
    color: var(--navy);
    font-weight: 900;
  }
  .date-day {
    font-size: 46px;
    line-height: 1;
  }
  .date-month-year {
    font-size: 21px;
    line-height: 20px;
    font-weight: 700;
  }
  .venue {
    position: absolute;
    left: 0;
    bottom: 10px;
    width: 100%;
    text-align: center;
    color: var(--white);
    font-weight: 700;
    font-size: 17.5px;
    margin: 0;
  }
</style>
</head>
<body>
  <main class="flyer">
    <svg class="flyer-art" width="432" height="610" viewBox="0 0 432 610" aria-hidden="true">
      <defs>
        <radialGradient id="greenField" cx="0.4" cy="0.35" r="0.8">
          <stop offset="0" stop-color="var(--green-light)"/>
          <stop offset="0.6" stop-color="var(--green)"/>
          <stop offset="1" stop-color="var(--green-dark)"/>
        </radialGradient>
      </defs>
      <!-- green field with pointed header edge -->
      <polygon points="0,98 200,98 216,76 232,98 432,98 432,610 0,610" fill="url(#greenField)"/>
      <polyline points="0,98 200,98 216,76 232,98 432,98" fill="none" stroke="var(--navy)" stroke-width="2"/>
      <!-- layered banner -->
      <polygon points="6,252 216,350 414,240 402,540 26,540" fill="var(--slate-light)"/>
      <polygon points="10,248 216,344 410,236 398,540 32,540" fill="var(--navy-dark)"/>
      <polygon points="14,244 216,338 404,232 392,540 40,540" fill="var(--navy)" stroke="var(--white)" stroke-width="2.5"/>
      <polygon points="24,250 216,346 396,242 386,540 48,540" fill="var(--navy)"/>
      <!-- footer band -->
      <rect x="0" y="520" width="432" height="90" fill="var(--slate)"/>
    </svg>

    <header class="brand">
      <span class="brand-mark"></span>
      <span class="brand-name">Q-TarVM</span>
    </header>

    <h1 class="title">
      <span class="title-edition">4th Annual</span>
      <span class="title-name">Lift Her Forward</span>
      <span class="title-tagline">and See Her Rise!</span>
    </h1>

    <p class="save-date">Save the<br>date</p>

    <div class="date-card">
      <span class="date-day">25</span>
      <span class="date-month-year">January<br>2019</span>
    </div>

    <p class="venue">Harbor Crest Resort and Spa, San Marcos, TX</p>
  </main>
</body>
</html>
```